Business Card Design For Office Furniture Clearance Company

Kestrel Office Clearance - our company name pretty much explains what we do, we clear offices for high end clients, mainly plc's and large international companies.

We require a nice looking business card that displays professionalism but without being too serious.

It would be nice to see just a little more than a conventional boring business card, make sure you add some flare.

Industry/Entity Type

Office Furniture

Contact Information for Business Card

CARD 1

Tom Pardew
Director
tom@kestrelofficeclearance.co.uk
m: 07700 513928

t: 01632 419063
www.kestrelofficeclearance.co.uk

Kestrel Office Clearance
Unit K4 B
3-7 Ferndale Lane
Ashcombe
Wrenford Vale
ZZ9 4QX

free office clearances… you cant get better than that.

CARD 2

Henry Walbrook
Director
henry@kestrelofficeclearance.co.uk
m: 07700 628157

t: 01632 419063

Kestrel Office Clearance
Unit K4 B
3-7 Ferndale Lane
Ashcombe
Wrenford Vale
ZZ9 4QX

Font styles to use
Sans Serif

Requirements
Must have
• A white background - as we have a blue logo.
Nice to have
• Nice use of the logo - play around with this and dissect it.

```html
<!DOCTYPE html>
<html lang="en">
<head>
<meta charset="utf-8">
<title>Kestrel Office Clearance — Business Cards</title>
<link rel="stylesheet" href="https://fonts.googleapis.com/css2?family=Montserrat:wght@400;500;600;700&display=swap">
<style>
  :root {
    --stage: #e7e8ea;
    --card: #ffffff;
    --brand-blue: #1a7bbd;
    --brand-blue-deep: #1f5f93;
    --ink: #1d1d1f;
    --ink-soft: #4a4a4f;
    --flame-warm: #f6c98a;
    --flame-light: #fbe6c8;
  }
  * { box-sizing: border-box; margin: 0; padding: 0; }
  html, body {
    width: 1200px; height: 900px; overflow: hidden;
    background: var(--stage);
    font-family: "Montserrat", Arial, sans-serif;
  }
  .stage { position: relative; width: 1200px; height: 900px; }

  .card {
    position: absolute;
    width: 560px; height: 330px;
    background: var(--card);
    border-radius: 22px;
    box-shadow: 0 10px 28px rgba(0,0,0,.16);
    overflow: hidden;
  }

  /* Front */
  .card--front { left: 70px; top: 80px; }
  .front-flare {
    position: absolute; right: 18px; top: 14px;
    width: 165px; height: 150px;
    border-radius: 60% 40% 50% 50%;
    background: radial-gradient(ellipse at 40% 60%, var(--flame-warm) 0%, var(--flame-light) 45%, rgba(255,255,255,0) 75%);
    opacity: .6;
  }
  .front-mark {
    position: absolute; left: 0; right: 0; top: 46px;
    display: flex; flex-direction: column; align-items: center; gap: 14px;
  }
  .front-mark .mark-dot {
    width: 150px; height: 150px; border-radius: 50%;
    background: var(--brand-blue);
  }
  .front-mark .brand-name {
    font-weight: 700; font-size: 20px; color: var(--brand-blue);
  }
  .front-tagline {
    position: absolute; left: 0; right: 0; bottom: 26px;
    text-align: center;
    font-weight: 500; font-size: 13px; letter-spacing: 1.2px;
    color: var(--ink);
  }

  /* Back */
  .card--back { left: 570px; top: 480px; }
  .back-mark {
    position: absolute; right: 34px; top: 26px;
    display: flex; flex-direction: column; align-items: center; gap: 10px;
  }
  .back-mark .mark-dot {
    width: 108px; height: 108px; border-radius: 50%;
    background: var(--brand-blue);
  }
  .back-mark .brand-name {
    font-weight: 700; font-size: 11px; letter-spacing: .3px; color: var(--ink);
    text-transform: uppercase;
  }
  .rule {
    position: absolute; left: 40px; right: 30px; top: 176px;
    height: 2px; background: var(--brand-blue-deep);
  }
  .person { position: absolute; left: 40px; top: 128px; }
  .person-name {
    font-weight: 700; font-size: 21px; color: var(--brand-blue);
    text-transform: uppercase; line-height: 1.1;
  }
  .person-role {
    font-weight: 500; font-size: 12px; color: var(--ink-soft);
    text-transform: uppercase; letter-spacing: .5px;
  }
  .address {
    position: absolute; right: 40px; top: 190px;
    font-size: 13px; line-height: 1.35; color: var(--ink-soft);
    list-style: none;
  }
  .contacts {
    position: absolute; left: 40px; bottom: 24px;
    list-style: none; font-size: 13px; color: var(--ink); line-height: 1.45;
  }
  .contacts li { display: flex; align-items: center; gap: 10px; }
  .contacts svg { width: 12px; height: 12px; flex: none; }
  .contacts svg * { stroke: var(--brand-blue); fill: none; stroke-width: 1.6; }
</style>
</head>
<body>
<main class="stage">

  <section class="card card--front" aria-label="Card front">
    <div class="front-flare" role="img" aria-label="Soft warm flame flourish"></div>
    <div class="front-mark">
      <span class="mark-dot"></span>
      <span class="brand-name">Kestrel Office Clearance</span>
    </div>
    <p class="front-tagline">FREE OFFICE CLEARANCES... YOU CANT GET BETTER THAN THAT</p>
  </section>

  <section class="card card--back" aria-label="Card back">
    <div class="back-mark">
      <span class="mark-dot"></span>
      <span class="brand-name">Kestrel Office Clearance</span>
    </div>

    <div class="person">
      <p class="person-name">Tom Pardew</p>
      <p class="person-role">Director</p>
    </div>
    <div class="rule"></div>

    <ul class="address">
      <li>Kestrel Office Clearance</li>
      <li>Unit K4 B</li>
      <li>3-7 Ferndale Lane</li>
      <li>Ashcombe</li>
      <li>Wrenford Vale</li>
      <li>ZZ9 4QX</li>
    </ul>

    <ul class="contacts">
      <li>
        <svg viewBox="0 0 12 12"><rect x="3" y="1" width="6" height="10" rx="1"/></svg>
        07700 513928
      </li>
      <li>
        <svg viewBox="0 0 12 12"><path d="M2 2c0 5 3 8 8 8l1-2-2-1-1 1c-2-1-3-2-4-4l1-1-1-2z"/></svg>
        01632 419063
      </li>
      <li>
        <svg viewBox="0 0 12 12"><rect x="1" y="2.5" width="10" height="7"/><path d="M1 2.5l5 4 5-4"/></svg>
        tom@kestrelofficeclearance.co.uk
      </li>
      <li>
        <svg viewBox="0 0 12 12"><circle cx="6" cy="6" r="5"/><path d="M1 6h10M6 1c-2 3-2 7 0 10M6 1c2 3 2 7 0 10"/></svg>
        www.kestrelofficeclearance.co.uk
      </li>
    </ul>
  </section>

</main>
</body>
</html>
```